Mavro Scrub - Contact/Landing Page

I need a landing page which will essentially be the page that customers will go to from the 'website' link on GMB listing. It will provide a short overview of services which need to be selectable. a little further down can capture some contact details followed by a large Submit Now button etc...

I have some icon/logo's that can be utilised at the bottom of the page as industry type references.

Target Market(s)

End of Lease Cleaning Services

Industry/Entity Type

Cleaning Service

Colors

Designer to choose colors to be used in the design.

Requirements
Must have
• As per description
Should not have
• Colours to match my website mavroscrub.com.au

```html
<!DOCTYPE html>
<html lang="en">
<head>
<meta charset="utf-8">
<title>Mavro Scrub – End of Lease Services</title>
<link rel="stylesheet" href="https://fonts.googleapis.com/css2?family=Source+Sans+3:wght@400;600;700&family=Crimson+Text&family=Arimo&display=swap">
<style>
  :root {
    --brand-blue: #0872c8;
    --accent-blue: #2f9bdc;
    --ink: #111111;
    --soft-band: #e5f1fa;
    --field-border: #b9c3cc;
    --footer-bg: #2b2b2b;
    --white: #ffffff;
    --icon-dark: #1d1d1d;
  }
  * { box-sizing: border-box; margin: 0; padding: 0; }
  html, body { width: 733px; height: 1200px; overflow: hidden; }
  body { position: relative; background: var(--white); font-family: "Source Sans 3", sans-serif; color: var(--ink); }

  .site-header { position: absolute; left: 0; top: 0; width: 733px; height: 250px; background: var(--brand-blue); }
  .menu-toggle { position: absolute; left: 57px; top: 21px; width: 17px; height: 13px; }
  .menu-toggle span { display: block; height: 2px; background: var(--white); margin-bottom: 3.5px; }
  .header-phone { position: absolute; right: 26px; top: 22px; display: flex; align-items: center; gap: 7px; color: var(--white); font-weight: 700; font-size: 15px; }
  .brand { position: absolute; left: 0; top: 110px; width: 733px; display: flex; justify-content: center; align-items: center; gap: 10px; }
  .brand-dot { width: 26px; height: 26px; border-radius: 50%; background: var(--white); }
  .brand-name { color: var(--white); font-weight: 700; font-size: 36px; letter-spacing: 0.5px; }
  .tagline { position: absolute; left: 0; top: 187px; width: 733px; text-align: center; color: var(--white); font-family: "Crimson Text", serif; font-size: 19px; }
  .tagline .divider { display: inline-block; width: 1.5px; height: 20px; background: var(--white); vertical-align: -4px; margin: 0 8px; }

  .services-title { position: absolute; top: 305px; width: 733px; text-align: center; font-size: 25px; font-weight: 400; letter-spacing: 0.3px; }
  .services-intro { position: absolute; top: 344px; width: 733px; text-align: center; font-family: "Arimo", sans-serif; font-size: 11px; line-height: 16px; }
  .service { position: absolute; top: 414px; width: 150px; text-align: center; }
  .service-icon { width: 66px; height: 66px; margin: 0 auto; border-radius: 8px; background: #d9d9d9; }
  .service-name { margin-top: 14px; font-size: 12.5px; font-weight: 700; letter-spacing: 0.3px; }
  .service-text { margin-top: 6px; font-family: "Arimo", sans-serif; font-size: 7.5px; line-height: 14.5px; }
  .service-select { margin-top: 6px; font-size: 8px; font-weight: 700; display: flex; justify-content: center; align-items: center; gap: 5px; }
  .checkbox { width: 9px; height: 9px; border: 1px solid #333; border-radius: 1px; }
  .service.is-selected { color: var(--brand-blue); }
  .service.is-selected .service-icon { background: #b8d6ef; }
  .checkbox.is-checked { border: none; }

  .contact-band { position: absolute; top: 622px; left: 0; width: 733px; height: 258px; background: var(--soft-band); }
  .field { position: absolute; left: 161px; width: 212px; height: 25px; background: var(--white); border: 1px solid var(--field-border); font-size: 7px; padding-left: 10px; line-height: 23px; }
  .submit-button { position: absolute; left: 428px; top: 105px; width: 213px; height: 48px; border-radius: 24px; background: var(--brand-blue); color: var(--white); font-weight: 700; font-size: 17px; text-align: center; line-height: 48px; letter-spacing: 0.2px; }

  .partners-title { position: absolute; top: 921px; width: 733px; text-align: center; color: var(--accent-blue); font-weight: 700; font-size: 24px; }
  .partners-sub { position: absolute; top: 953px; width: 733px; text-align: center; font-size: 11px; }
  .badge { position: absolute; top: 989px; width: 134px; height: 66px; background: var(--white); box-shadow: 0 1px 4px rgba(0,0,0,0.25); display: flex; align-items: center; justify-content: center; }
  .badge-shape { border-radius: 3px; }
  .carousel-dots { position: absolute; top: 1080px; left: 0; width: 733px; display: flex; justify-content: center; gap: 5px; }
  .carousel-dots span { width: 9px; height: 9px; border-radius: 50%; border: 1.3px solid #222; }
  .carousel-dots .is-active { width: 10px; height: 10px; border-color: var(--accent-blue); }

  .site-footer { position: absolute; top: 1151px; left: 0; width: 733px; height: 49px; background: var(--footer-bg); color: var(--white); font-size: 8.5px; font-weight: 600; text-align: center; line-height: 49px; }
</style>
</head>
<body>
  <header class="site-header">
    <div class="menu-toggle"><span></span><span></span><span></span></div>
    <div class="header-phone">
      <svg width="19" height="19" viewBox="0 0 20 20" aria-hidden="true">
        <circle cx="10" cy="10" r="9" fill="none" stroke="#fff" stroke-width="1.6"/>
        <path d="M6.5 5.5c.6-.5 1.3-.4 1.6.1l.9 1.5c.3.5.1 1-.3 1.3l-.5.4c.5 1.3 1.4 2.3 2.6 2.9l.4-.5c.3-.4.9-.5 1.3-.2l1.5 1c.5.3.5 1 .1 1.5-.7.9-1.8 1.2-2.8.7C8.8 13 6.9 11 6 8.6c-.4-1.1-.2-2.3.5-3.1z" fill="#fff"/>
      </svg>
      <span>0400 123 456</span>
    </div>
    <div class="brand">
      <span class="brand-dot"></span>
      <span class="brand-name">Mavro Scrub</span>
    </div>
    <p class="tagline">End of Lease Cleaning<span class="divider"></span>Licensed Pest Control</p>
  </header>

  <main>
    <section class="services">
      <h1 class="services-title">END OF LEASE SERVICES</h1>
      <p class="services-intro">Fusce tempor odio quis tellus tempor, et commodo purus lobortis.<br>Morbi nec ante faucibus, fermentum neque quis</p>

      <div class="service" style="left:92px">
        <div class="service-icon" role="img" aria-label="Cleaning bucket with spray bottles and sponge icon"></div>
        <h2 class="service-name">CLEANING</h2>
        <p class="service-text">Lorem ipsum dolor sit amet, consectetur adipiscing elit, sed do eiusmod tempor incididunt ut labore</p>
        <div class="service-select">Select <span class="checkbox"></span></div>
      </div>

      <div class="service is-selected" style="left:292px">
        <div class="service-icon" role="img" aria-label="Carpet cleaning machine icon"></div>
        <h2 class="service-name">CARPET CLEANING</h2>
        <p class="service-text">Lorem ipsum dolor sit amet, consectetur adipiscing elit, sed do eiusmod tempor incididunt ut labore</p>
        <div class="service-select">Select
          <svg class="checkbox is-checked" width="10" height="10" viewBox="0 0 10 10" aria-hidden="true">
            <rect width="10" height="10" rx="1.5" fill="#2f5fe0"/>
            <path d="M2.2 5.2l1.9 1.9 3.8-4" fill="none" stroke="#fff" stroke-width="1.4"/>
          </svg>
        </div>
      </div>

      <div class="service" style="left:490px">
        <div class="service-icon" role="img" aria-label="Fly insect pest control icon"></div>
        <h2 class="service-name">PEST CONTROL</h2>
        <p class="service-text">Lorem ipsum dolor sit amet, consectetur adipiscing elit, sed do eiusmod tempor incididunt ut labore</p>
        <div class="service-select">Select <span class="checkbox"></span></div>
      </div>
    </section>

    <section class="contact-band">
      <div class="field" style="top:42px">First Name</div>
      <div class="field" style="top:80px">Sur Name</div>
      <div class="field" style="top:117px">Phone</div>
      <div class="field" style="top:155px">Email</div>
      <div class="field" style="top:192px">Subject</div>
      <div class="submit-button">SUBMIT NOW</div>
    </section>

    <section class="partners">
      <h2 class="partners-title">Lorem ipsum dolor sit amet,</h2>
      <p class="partners-sub">Sed ut perspiciatis unde omnis iste natus error sit</p>
      <div class="badge" style="left:87px"><div class="badge-shape" style="width:134px;height:66px;background:#7dbd2a;border-radius:0"></div></div>
      <div class="badge" style="left:228px"><div class="badge-shape" style="width:110px;height:30px;background:#d8dbe8"></div></div>
      <div class="badge" style="left:369px"><div class="badge-shape" style="width:106px;height:40px;background:#111"></div></div>
      <div class="badge" style="left:509px"><div class="badge-shape" style="width:70px;height:44px;background:#2a4aa0"></div></div>
      <div class="carousel-dots"><span class="is-active"></span><span></span><span></span><span></span></div>
    </section>
  </main>

  <footer class="site-footer">Mavro Scrub © 2021 All Rights Reserved</footer>
</body>
</html>
```